amber crest health and wellness group.

need a full website design , all information provided in word document labeled website blue print

Target Market(s)

first responders, military , people in crisis

Coding

Coded - Design and coding required

Number of Pages Required

1 page

```html
<!DOCTYPE html>
<html lang="en">
<head>
<meta charset="utf-8">
<title>Amber Crest Health &amp; Wellness Group</title>
<link rel="stylesheet" href="https://fonts.googleapis.com/css2?family=Michroma&family=Poppins:wght@300;400;500;600&display=swap">
<style>
:root{
  --navy:#1c2f5f;
  --navy-deep:#121f45;
  --ink:#1e2430;
  --muted:#4a5262;
  --sky:#e2eaf7;
  --white:#ffffff;
  --black:#050608;
  --line:#c9d3e6;
}
*{box-sizing:border-box;margin:0;padding:0}
html,body{width:1200px;height:5340px;overflow:hidden}
body{font-family:'Poppins',sans-serif;color:var(--ink);background:var(--white);position:relative}
.display{font-family:'Michroma',sans-serif;text-transform:uppercase;letter-spacing:1px}
section,header,footer{position:relative;width:1200px;overflow:hidden}
.btn{display:inline-block;font-family:'Michroma',sans-serif;font-size:12px;letter-spacing:.5px;padding:12px 24px;border-radius:24px;text-decoration:none}
.btn-light{background:var(--white);color:var(--navy)}
.btn-navy{background:var(--navy);color:var(--white)}
.btn-outline{border:1.5px solid var(--navy);color:var(--navy);background:var(--white)}

/* hero */
.hero{height:860px;background:#7a8794}
.hero-photo{position:absolute;inset:0;background:linear-gradient(100deg,#2a3446 0%,#5d6a78 35%,#c9b9a6 65%,#e9e0d3 100%)}
.topbar{position:absolute;top:0;left:0;right:0;height:130px;display:flex;align-items:center;padding:0 56px;z-index:2}
.brand{display:flex;align-items:center;gap:12px;color:var(--white)}
.brand-mark{width:18px;height:18px;background:var(--white);border-radius:50%}
.brand-name{font-family:'Poppins',sans-serif;font-weight:600;font-size:22px;line-height:1.1}
.brand-name small{display:block;font-size:9px;font-weight:600;letter-spacing:1.5px}
.nav{margin-left:auto;text-align:right}
.nav-phone{font-family:'Michroma',sans-serif;font-size:13px;color:var(--white);display:flex;align-items:center;gap:8px;justify-content:flex-end;margin-bottom:16px}
.nav-links{display:flex;gap:36px;list-style:none}
.nav-links a{font-family:'Michroma',sans-serif;font-size:12px;color:var(--white);text-decoration:none;padding-bottom:6px}
.nav-links .active{border-bottom:2px solid var(--white)}
.hero-copy{position:absolute;left:56px;top:270px;color:var(--white);z-index:2;width:760px}
.hero-copy h1{font-size:36px;line-height:1.3;margin-bottom:18px;white-space:nowrap}
.hero-copy p{font-size:15px;font-weight:500;line-height:1.5;margin-bottom:34px;width:600px}
.hero-wave{position:absolute;left:0;bottom:0;width:1200px;height:260px;z-index:1}

/* section titles */
.sec-title{text-align:center}
.sec-title h2{font-size:34px;color:var(--navy)}
.sec-title span{display:block;font-size:11px;color:var(--muted);letter-spacing:2px;margin-top:6px;font-family:'Michroma',sans-serif}

/* who we serve */
.serve{height:660px;padding-top:50px}
.serve-intro{width:820px;margin:30px auto 46px;text-align:center;font-size:14px;line-height:1.6;color:var(--muted)}
.serve-track{display:flex;justify-content:center;gap:30px;position:relative}
.serve-card{width:280px;height:340px;background:var(--white);border-radius:14px;box-shadow:0 6px 22px rgba(20,30,60,.15);overflow:hidden}
.serve-card .photo{height:150px}
.serve-card .body{padding:16px 22px;text-align:center}
.serve-card h3{font-size:15px;font-weight:600;margin-bottom:8px}
.serve-card p{font-size:12px;line-height:1.55;color:var(--muted);margin-bottom:12px}
.serve-card a{font-size:12px;color:var(--navy);text-decoration:underline}
.arrow{position:absolute;top:150px;width:36px;height:36px;border-radius:50%;display:flex;align-items:center;justify-content:center}
.arrow-left{left:100px;background:var(--line)}
.arrow-right{right:100px;background:var(--navy)}

/* about */
.about{height:960px;background:var(--sky)}
.about-wave-top,.about-wave-bottom{position:absolute;left:0;width:1200px}
.about-wave-top{top:0;height:120px}
.about-wave-bottom{bottom:0;height:120px}
.about-head{position:absolute;left:640px;top:140px;width:520px}
.about-head h2{font-size:27px;color:var(--navy);text-align:left;white-space:nowrap}
.about-head span{font-family:'Michroma',sans-serif;font-size:11px;color:var(--muted);letter-spacing:2px}
.about-photo{position:absolute;left:170px;top:160px;width:340px;height:340px;border-radius:50%;background:linear-gradient(180deg,#7fb3e6 0%,#b7d4ef 45%,#4f7f5e 75%,#2f5a3d 100%)}
.about-text{position:absolute;left:640px;top:230px;width:440px;font-size:13px;line-height:1.65;color:var(--ink)}
.about-text p{margin-bottom:14px}
.mv{position:absolute;top:560px;width:440px;height:250px;border-radius:16px;padding:28px 30px;color:var(--white)}
.mv-mission{left:150px;background:var(--navy)}
.mv-vision{left:630px;background:#878c96}
.mv-head{display:flex;align-items:center;gap:18px;margin-bottom:16px}
.mv-icon{width:56px;height:56px;border-radius:50%;background:var(--white);display:flex;align-items:center;justify-content:center;flex:none}
.mv h3{font-size:20px}
.mv p{font-size:12.5px;line-height:1.6}

/* services */
.offer{height:1880px;padding-top:30px}
.service{position:absolute;left:0;width:1200px;height:560px}
.service h3{font-size:30px;font-weight:400;color:var(--ink);margin-bottom:8px}
.service .lead{font-size:13px;line-height:1.55;color:var(--muted);margin-bottom:16px}
.service h4{font-size:15px;font-weight:600;color:var(--navy);margin-bottom:12px}
.ticks{list-style:none;margin-bottom:22px}
.ticks li{display:flex;align-items:center;gap:12px;font-size:14px;font-weight:500;margin-bottom:12px}
.ticks svg{flex:none}
.svc-photo{position:absolute;width:440px;height:500px;border-radius:16px}
.svc-text{position:absolute;width:440px}
.s1{top:130px}.s1 .svc-text{left:150px;top:20px}.s1 .svc-photo{left:640px;top:0;background:linear-gradient(135deg,#c8b8a6,#8d7a68 55%,#4d4439)}
.s2{top:730px}.s2 .svc-photo{left:150px;top:0;background:linear-gradient(135deg,#3a2e28,#6c5344 50%,#1e1916)}.s2 .svc-text{left:660px;top:60px}
.s3{top:1320px}.s3 .svc-text{left:150px;top:20px}.s3 .svc-photo{left:640px;top:0;background:linear-gradient(135deg,#e6a96a,#b0673a 50%,#5e3320)}

/* contact band */
.contact{height:400px;background:linear-gradient(180deg,#3c414c,#262a33)}
.contact-inner{position:absolute;top:60px;left:0;right:0;text-align:center;color:var(--white)}
.contact h2{font-size:32px}
.contact span{font-family:'Michroma',sans-serif;font-size:11px;letter-spacing:2px;display:block;margin:6px 0 18px}
.contact p{width:760px;margin:0 auto 22px;font-size:13px;line-height:1.6}
.contact-wave{position:absolute;bottom:0;left:0;width:1200px;height:110px}

/* footer */
.footer{height:580px;background:var(--black);color:var(--white)}
.footer-brand{position:absolute;left:130px;top:90px;display:flex;align-items:center;gap:14px}
.footer-brand .brand-mark{width:22px;height:22px}
.footer-brand .brand-name{font-size:26px}
.footer-col{position:absolute;top:80px}
.footer-col h5{font-family:'Michroma',sans-serif;font-size:15px;font-weight:400;margin-bottom:20px}
.footer-col ul{list-style:none}
.footer-col li{font-size:13px;color:#c8ccd4;margin-bottom:10px}
.fc1{left:500px}.fc2{left:720px}.fc3{left:940px}
.copyright{position:absolute;bottom:30px;left:0;right:0;text-align:center;font-size:12px;color:#b8bcc4;border-top:1px solid #222;padding-top:22px}
</style>
</head>
<body>

<header class="hero">
  <div class="hero-photo" role="img" aria-label="Photo of a smiling woman laughing outdoors in warm sunlight"></div>
  <div class="topbar">
    <div class="brand">
      <span class="brand-mark"></span>
      <div class="brand-name">Amber Crest<small>HEALTH &amp; WELLNESS GROUP</small></div>
    </div>
    <nav class="nav">
      <div class="nav-phone">
        <svg width="14" height="14" viewBox="0 0 24 24" fill="#fff"><path d="M6.6 10.8a15 15 0 0 0 6.6 6.6l2.2-2.2c.3-.3.7-.4 1-.2 1.1.4 2.3.6 3.6.6.6 0 1 .4 1 1V20c0 .6-.4 1-1 1A17 17 0 0 1 3 4c0-.6.4-1 1-1h3.5c.6 0 1 .4 1 1 0 1.3.2 2.5.6 3.6.1.3 0 .7-.2 1z"/></svg>
        CALL US: +1 555 010 2040
      </div>
      <ul class="nav-links">
        <li><a class="active" href="#">Home</a></li>
        <li><a href="#">About</a></li>
        <li><a href="#">Services</a></li>
        <li><a href="#">Our Team</a></li>
        <li><a href="#">FAQ</a></li>
        <li><a href="#">Contact</a></li>
      </ul>
    </nav>
  </div>
  <div class="hero-copy">
    <h1 class="display">Helping Those<br>Who Help Others</h1>
    <p>Compassionate, science-based mental health &amp; wellness services designed for first responders, frontline professionals, and communities.</p>
    <a class="btn btn-light" href="#">Book a Consultation</a>
  </div>
  <svg class="hero-wave" viewBox="0 0 1200 260" preserveAspectRatio="none">
    <path d="M0 150 C300 260 700 40 1200 120 L1200 260 L0 260Z" fill="var(--navy)"/>
    <path d="M0 175 C320 270 720 70 1200 150 L1200 260 L0 260Z" fill="var(--white)"/>
  </svg>
</header>

<section class="serve">
  <div class="sec-title"><h2 class="display">Who We Serve</h2><span>AMBER CREST</span></div>
  <p class="serve-intro">At Amber Crest Health &amp; Wellness Group, we proudly support a diverse community of individuals who dedicate their lives to protecting, caring for, and uplifting others.</p>
  <div class="serve-track">
    <div class="arrow arrow-left"><svg width="14" height="14" viewBox="0 0 24 24"><path d="M15 5l-7 7 7 7" stroke="#fff" stroke-width="3" fill="none"/></svg></div>
    <article class="serve-card">
      <div class="photo" role="img" aria-label="Photo of military service members" style="background:linear-gradient(135deg,#8a8466,#5b5a44)"></div>
      <div class="body">
        <h3>Military Members &amp; Veterans</h3>
        <p>We offer confidential, specialized care for military personnel and veterans coping with trauma, transition stress, service-related injuries, or mental health challenges.</p>
        <a href="#">Read More</a>
      </div>
    </article>
    <article class="serve-card">
      <div class="photo" role="img" aria-label="Photo of healthcare professionals with a patient" style="background:linear-gradient(135deg,#b9c7d6,#7f93a8)"></div>
      <div class="body">
        <h3>Healthcare Professionals</h3>
        <p>Nurses, physicians, PSWs, technicians, and frontline hospital staff face immense pressures. We provide targeted services to reduce burnout, support emotional well-being, and strengthen long-term resilience.</p>
        <a href="#">Read More</a>
      </div>
    </article>
    <article class="serve-card">
      <div class="photo" role="img" aria-label="Photo of a smiling family group outdoors" style="background:linear-gradient(135deg,#b6a27c,#7b6a4c)"></div>
      <div class="body">
        <h3>Individuals &amp; Families</h3>
        <p>We offer mental health therapy and wellness services for adults, teens, couples, and families seeking support for anxiety, trauma, stress, life transitions, or emotional wellness.</p>
        <a href="#">Read More</a>
      </div>
    </article>
    <div class="arrow arrow-right"><svg width="14" height="14" viewBox="0 0 24 24"><path d="M9 5l7 7-7 7" stroke="#fff" stroke-width="3" fill="none"/></svg></div>
  </div>
</section>

<section class="about">
  <svg class="about-wave-top" viewBox="0 0 1200 120" preserveAspectRatio="none">
    <path d="M0 0 H1200 V40 C800 120 400 0 0 60Z" fill="var(--white)"/>
    <path d="M0 60 C400 0 800 120 1200 40 V55 C800 135 400 15 0 75Z" fill="var(--navy)"/>
  </svg>
  <div class="about-photo" role="img" aria-label="Aerial photo of a city skyline beside green parkland"></div>
  <div class="about-head"><h2 class="display">About Amber Crest</h2><span>HEALTH &amp; WELLNESS GROUP</span></div>
  <div class="about-text">
    <p>Amber Crest Health &amp; Wellness Group was created with a clear purpose: to provide compassionate, evidence-based support for the people who dedicate their lives to serving our communities. Opening in March 2026 in Port Haldane, Ontario, our centre brings together a multidisciplinary team of clinicians, therapists, and wellness professionals who share a commitment to trauma-informed care, respect, and integrity.</p>
    <p>We recognize the unique challenges faced by first responders, frontline professionals, military members, and healthcare workers—along with the individuals and families who support them.</p>
    <a class="btn btn-navy" href="#">Join Our Team</a>
  </div>
  <div class="mv mv-mission">
    <div class="mv-head">
      <div class="mv-icon"><svg width="28" height="28" viewBox="0 0 24 24"><circle cx="12" cy="12" r="9" stroke="var(--navy)" stroke-width="2" fill="none"/><circle cx="12" cy="12" r="4" fill="var(--navy)"/></svg></div>
      <h3 class="display">Our Mission</h3>
    </div>
    <p>Our mission is to provide compassionate, evidence-based mental health and wellness services that support and empower the people who serve our communities. We are committed to delivering trauma-informed care, integrated therapeutic modalities, and a safe, confidential environment where first responders, frontline professionals, individuals, and families can heal, recover, and thrive.</p>
  </div>
  <div class="mv mv-vision">
    <div class="mv-head">
      <div class="mv-icon"><svg width="30" height="30" viewBox="0 0 24 24"><path d="M2 12s4-7 10-7 10 7 10 7-4 7-10 7S2 12 2 12z" stroke="#878c96" stroke-width="2" fill="none"/><circle cx="12" cy="12" r="3" fill="#878c96"/></svg></div>
      <h3 class="display">Our Vision</h3>
    </div>
    <p>Our vision is to become a leading centre of excellence for trauma-focused mental health and wellness in Ontario. We aim to build a community where every individual—especially those who dedicate their lives to protecting and caring for others—has steady access to high-quality support, innovative therapies, and restorative care.</p>
  </div>
  <svg class="about-wave-bottom" viewBox="0 0 1200 120" preserveAspectRatio="none">
    <path d="M0 40 C400 120 800 0 1200 70 V85 C800 15 400 135 0 55Z" fill="var(--navy)"/>
    <path d="M0 55 C400 135 800 15 1200 85 V120 H0Z" fill="var(--white)"/>
  </svg>
</section>

<section class="offer">
  <div class="sec-title"><h2 class="display">What We Offer</h2><span>SERVICES</span></div>

  <div class="service s1">
    <div class="svc-text">
      <h3>Mental Health Therapy</h3>
      <p class="lead">Evidence-based counselling for individuals, couples, and families. Our clinicians provide a safe, confidential space to explore challenges, build resilience, and support long-term well-being.</p>
      <h4>Common areas of support:</h4>
      <ul class="ticks">
        <li><svg width="20" height="20" viewBox="0 0 20 20"><circle cx="10" cy="10" r="10" fill="var(--navy)"/><path d="M5.5 10.5l3 3 6-6" stroke="#fff" stroke-width="2" fill="none"/></svg>Anxiety, depression, stress</li>
        <li><svg width="20" height="20" viewBox="0 0 20 20"><circle cx="10" cy="10" r="10" fill="var(--navy)"/><path d="M5.5 10.5l3 3 6-6" stroke="#fff" stroke-width="2" fill="none"/></svg>Trauma &amp; PTSD</li>
        <li><svg width="20" height="20" viewBox="0 0 20 20"><circle cx="10" cy="10" r="10" fill="var(--navy)"/><path d="M5.5 10.5l3 3 6-6" stroke="#fff" stroke-width="2" fill="none"/></svg>Relationship concerns</li>
        <li><svg width="20" height="20" viewBox="0 0 20 20"><circle cx="10" cy="10" r="10" fill="var(--navy)"/><path d="M5.5 10.5l3 3 6-6" stroke="#fff" stroke-width="2" fill="none"/></svg>Workplace stress</li>
        <li><svg width="20" height="20" viewBox="0 0 20 20"><circle cx="10" cy="10" r="10" fill="var(--navy)"/><path d="M5.5 10.5l3 3 6-6" stroke="#fff" stroke-width="2" fill="none"/></svg>Grief &amp; loss</li>
        <li><svg width="20" height="20" viewBox="0 0 20 20"><circle cx="10" cy="10" r="10" fill="var(--navy)"/><path d="M5.5 10.5l3 3 6-6" stroke="#fff" stroke-width="2" fill="none"/></svg>Life transitions</li>
      </ul>
      <a class="btn btn-outline" href="#">Read More</a>
    </div>
    <div class="svc-photo" role="img" aria-label="Photo of two women talking during a therapy session"></div>
  </div>

  <div class="service s2">
    <div class="svc-photo" role="img" aria-label="Photo of a woman comforting a friend"></div>
    <div class="svc-text">
      <h3>Trauma &amp; First Responder Support</h3>
      <p class="lead">Specialized clinical care for those working in high-intensity environments.</p>
      <h4>Our team is trained in:</h4>
      <ul class="ticks">
        <li><svg width="20" height="20" viewBox="0 0 20 20"><circle cx="10" cy="10" r="10" fill="var(--navy)"/><path d="M5.5 10.5l3 3 6-6" stroke="#fff" stroke-width="2" fill="none"/></svg>Operational Stress Injuries (OSI)</li>
        <li><svg width="20" height="20" viewBox="0 0 20 20"><circle cx="10" cy="10" r="10" fill="var(--navy)"/><path d="M5.5 10.5l3 3 6-6" stroke="#fff" stroke-width="2" fill="none"/></svg>Critical incident stress recovery</li>
        <li><svg width="20" height="20" viewBox="0 0 20 20"><circle cx="10" cy="10" r="10" fill="var(--navy)"/><path d="M5.5 10.5l3 3 6-6" stroke="#fff" stroke-width="2" fill="none"/></svg>First-responder culture &amp; lived realities</li>
        <li><svg width="20" height="20" viewBox="0 0 20 20"><circle cx="10" cy="10" r="10" fill="var(--navy)"/><path d="M5.5 10.5l3 3 6-6" stroke="#fff" stroke-width="2" fill="none"/></svg>PTSD &amp; cumulative trauma</li>
        <li><svg width="20" height="20" viewBox="0 0 20 20"><circle cx="10" cy="10" r="10" fill="var(--navy)"/><path d="M5.5 10.5l3 3 6-6" stroke="#fff" stroke-width="2" fill="none"/></svg>Burnout, compassion fatigue, and moral injury</li>
      </ul>
      <a class="btn btn-outline" href="#">Read More</a>
    </div>
  </div>

  <div class="service s3">
    <div class="svc-text">
      <h3>Salt Therapy (Halotherapy)</h3>
      <p class="lead">A natural wellness treatment using dry salt aerosol to support respiratory health, relaxation, and recovery.</p>
      <h4>Benefits:</h4>
      <ul class="ticks">
        <li><svg width="20" height="20" viewBox="0 0 20 20"><circle cx="10" cy="10" r="10" fill="var(--navy)"/><path d="M5.5 10.5l3 3 6-6" stroke="#fff" stroke-width="2" fill="none"/></svg>May improve breathing, sinus relief, and lung function</li>
        <li><svg width="20" height="20" viewBox="0 0 20 20"><circle cx="10" cy="10" r="10" fill="var(--navy)"/><path d="M5.5 10.5l3 3 6-6" stroke="#fff" stroke-width="2" fill="none"/></svg>Supports stress reduction and better sleep</li>
        <li><svg width="20" height="20" viewBox="0 0 20 20"><circle cx="10" cy="10" r="10" fill="var(--navy)"/><path d="M5.5 10.5l3 3 6-6" stroke="#fff" stroke-width="2" fill="none"/></svg>Gentle, meditative environment</li>
      </ul>
      <h4>What to expect:</h4>
      <p class="lead">Clients relax in a climate-controlled salt room designed for quiet sensory rest.</p>
      <a class="btn btn-outline" href="#">Read More</a>
    </div>
    <div class="svc-photo" role="img" aria-label="Photo of a woman relaxing in a warmly lit salt room"></div>
  </div>
</section>

<section class="contact" role="img" aria-label="Dimmed photo of a city skyline behind the contact message">
  <div class="contact-inner">
    <h2 class="display">Get In Touch With Us</h2>
    <span>CONTACT US</span>
    <p>Amber Crest Health &amp; Wellness Group was founded to address a growing need in our region: accessible, specialized support for individuals who experience intense stress, trauma exposure, and occupational demands. We saw that many first responders and frontline professionals struggled to find services that truly understood their culture, their environments, and their lived experiences.</p>
    <a class="btn btn-navy" href="#">Contact Us</a>
  </div>
  <svg class="contact-wave" viewBox="0 0 1200 110" preserveAspectRatio="none">
    <path d="M0 40 C400 110 800 0 1200 50 V110 H0Z" fill="var(--navy)"/>
    <path d="M0 62 C400 132 800 22 1200 72 V110 H0Z" fill="var(--black)"/>
  </svg>
</section>

<footer class="footer">
  <div class="footer-brand">
    <span class="brand-mark"></span>
    <div class="brand-name">Amber Crest<small>HEALTH &amp; WELLNESS GROUP</small></div>
  </div>
  <div class="footer-col fc1">
    <h5>Quick Links</h5>
    <ul><li>Home</li><li>About Us</li><li>Services</li><li>Our Team</li><li>Contact Us</li></ul>
  </div>
  <div class="footer-col fc2">
    <h5>Help Links</h5>
    <ul><li>FAQ</li><li>Support Links</li><li>Community Partners</li><li>Privacy Policy</li><li>Terms &amp; Conditions</li></ul>
  </div>
  <div class="footer-col fc3">
    <h5>Contact Us</h5>
    <ul><li>Location: Amber Crest</li><li>Port Haldane, Ontario</li><li>Phone: +1 555 010 2040</li><li>Email: info@ambercrest.example</li></ul>
  </div>
  <div class="copyright">Copyright©2025 Amber Crest. All Rights Reserved</div>
</footer>

</body>
</html>
```